Website Design for a holiday home letting busines

We require a redesign of our present website www.fernbrookstays.com. We want the website to stand out and look professional and clean to make holiday hunters want to book a caravan or lodge holiday with us. Our logo is red however we DO NOT want the website to be red. We want a natural colour scheme.

The final design should communicate that we are a professional company to book with.

On the home page we require;
Overview of company
Photo
Search box for holiday (check in)
Late Deals
Reviews
News

We would like the following pages designed; home page, available dates page, caravans page, content page.

The website should be responsive for smart phones. One website I do like is http://www.brimoveld.be/nl/

Target Market(s)

Families

Industry/Entity Type

Travel

Number of Pages Required

5+ page

Font styles to use
Serif

Requirements
Must have
• The project must be responsive for mobile phones and tablets.
• Ability to search for holiday home holidays
• We want a natural colour scheme.
Nice to have
• A style we like is http://www.brimoveld.be/nl/
Should not have
• Do not use red as a colour for the website. Our logo is red so this is the only time we want this used.

```html
<!DOCTYPE html>
<html lang="en">
<head>
<meta charset="utf-8">
<title>Fernbrook Stays – Private Holiday Rentals</title>
<link href="https://fonts.googleapis.com/css2?family=Open+Sans:wght@400;600;700&display=swap" rel="stylesheet">
<style>
:root{
  --teal:#1d8fa6;
  --teal-dark:#14707f;
  --ink:#333a40;
  --muted:#7a8288;
  --line:#d9dee2;
  --white:#ffffff;
  --footer:#2a2c2e;
  --footer-deep:#1d1f20;
}
*{box-sizing:border-box;margin:0;padding:0}
html,body{width:1200px;height:3196px;overflow:hidden}
body{font-family:"Open Sans",Arial,sans-serif;color:var(--ink);position:relative;background:#fff}
.backdrop{position:absolute;inset:0;background:linear-gradient(180deg,#4f9ad3 0,#7fbbe6 540px,#f4f8fb 640px,#ffffff 1200px,#d7ebf7 1300px,#9fd6e8 1700px,#4ec3cf 1900px,#8fd6d2 2150px,#e9efe6 2450px,#f2ece0 2520px)}
.site-header{position:absolute;top:0;left:0;width:1200px;height:88px;background:var(--white);box-shadow:0 1px 4px rgba(0,0,0,.12)}
.brand{position:absolute;left:160px;top:24px}
.brand-name{font-size:22px;font-weight:700;color:var(--ink);line-height:1}
.brand-tag{font-size:11px;color:var(--muted);margin-top:4px}
.header-search{position:absolute;right:160px;top:14px;display:flex;gap:8px}
.header-search span{display:block;width:120px;height:24px;border:1px solid var(--line);font-size:11px;color:var(--muted);padding:4px 8px;white-space:nowrap}
.main-nav{position:absolute;right:160px;top:54px;display:flex;gap:22px;font-size:12px;font-weight:600;text-transform:uppercase;white-space:nowrap}
.hero-photo{position:absolute;border:6px solid var(--white);box-shadow:0 4px 14px rgba(0,0,0,.25)}
.hero-main{left:160px;top:168px;width:440px;height:332px;background:linear-gradient(135deg,#e9e4dc,#b7aa98 60%,#8d8272)}
.hero-second{left:600px;top:300px;width:420px;height:300px;background:linear-gradient(135deg,#d8d2c7,#a38a6d 55%,#6f5b48)}
.hero-copy{position:absolute;left:668px;top:178px;width:380px}
.hero-copy h1{font-size:25px;color:var(--white);font-weight:700;letter-spacing:.5px;white-space:nowrap}
.hero-copy p{font-size:14px;color:#0f5c6e;font-weight:700;margin-top:6px;line-height:1.35}
.section-title{position:absolute;left:0;width:1200px;text-align:center;font-size:30px;font-weight:600;letter-spacing:1px;color:var(--ink)}
.section-title::after{content:"";display:block;width:60px;height:2px;background:var(--teal);margin:10px auto 0}
.deal-card{position:absolute;top:810px;width:260px;text-align:center}
.deal-photo{height:170px;background:linear-gradient(135deg,#eae7e2,#b9b0a4 60%,#80786d)}
.deal-card h3{font-size:14px;font-weight:600;margin:14px 0 12px;line-height:1.4}
.deal-meta{display:flex;justify-content:space-between;font-size:13px;color:var(--muted)}
.btn{display:inline-block;background:var(--teal);color:var(--white);font-weight:600;font-size:16px;border-radius:3px}
.deal-card .btn{width:120px;height:44px;line-height:44px;margin-top:18px}
.lodge-card{position:absolute;top:1380px;width:260px;height:330px;background:var(--white);box-shadow:0 2px 8px rgba(0,0,0,.15)}
.lodge-photo{height:185px;background:linear-gradient(135deg,#f2f0ec,#c2b7a8 60%,#7d9fb4)}
.view-badge{position:absolute;left:105px;top:160px;width:50px;height:50px;border-radius:50%;background:var(--teal);color:var(--white);border:3px solid var(--white);font-size:11px;font-weight:700;line-height:44px;text-align:center}
.lodge-card h3{text-align:center;font-size:15px;font-weight:600;margin-top:38px}
.lodge-meta{display:grid;grid-template-columns:1fr auto;gap:6px 10px;font-size:12px;color:var(--muted);padding:14px 20px 0}
.lodge-meta b{font-weight:400;color:var(--teal)}
.view-more{position:absolute;left:535px;top:1740px;width:130px;height:56px;line-height:56px;text-align:center;font-size:22px}
.live-chat{position:absolute;right:0;top:1380px;width:56px;height:180px;background:var(--teal);border-radius:8px 0 0 8px;color:var(--white);font-weight:700;font-size:17px;writing-mode:vertical-rl;transform:rotate(180deg);text-align:center;line-height:56px}
.review{position:absolute;width:420px}
.review h4{font-size:13px;font-weight:700;text-transform:uppercase}
.review .stay{font-size:13px;color:var(--teal);margin:4px 0}
.review p{font-size:12px;color:#50585e;line-height:1.5}
.blog-band{position:absolute;left:0;top:2520px;width:1200px;height:400px;background:linear-gradient(180deg,#cfe6f0,#8fd0dc 45%,#e6dcc6)}
.blog-intro{position:absolute;top:2630px;left:0;width:1200px;text-align:center;font-size:13px;color:#3f474d}
.blog-arrows{position:absolute;left:1000px;top:2562px;display:flex;gap:4px}
.blog-arrows span{width:18px;height:18px;background:#444;color:#fff;font-size:11px;line-height:18px;text-align:center}
.post{position:absolute;top:2668px;width:200px}
.post-photo{height:130px;background:linear-gradient(135deg,#e8e4dc,#b6a995 60%,#6e9db7)}
.post h5{font-size:12px;font-weight:600;margin:8px 0 4px}
.post p{font-size:11px;color:#4b5358;line-height:1.45}
.site-footer{position:absolute;left:0;top:2920px;width:1200px;height:240px;background:var(--footer);color:#c9cdd0}
.footer-col{position:absolute;top:28px}
.footer-col h6{font-size:16px;font-weight:600;color:var(--white);text-transform:uppercase;margin-bottom:14px}
.footer-col li{list-style:none;font-size:12px;line-height:21px}
.contact-row{display:flex;gap:8px;font-size:12px;line-height:1.5;margin-bottom:10px}
.contact-row svg{flex:none;margin-top:2px}
.feed-box{width:190px;height:130px;background:#f4f5f6;border:1px solid #bfc4c8}
.feed-head{height:40px;background:#e2e5e8;display:flex;align-items:center;gap:8px;padding:0 8px}
.feed-head i{width:26px;height:26px;background:#9aa3aa;display:block}
.feed-head span{font-size:11px;color:#333;font-style:normal}
.copyright{position:absolute;left:0;top:3160px;width:1200px;height:36px;background:var(--footer-deep);color:#a6abaf;font-size:11px;text-align:center;line-height:36px}
</style>
</head>
<body>
<div class="backdrop" role="img" aria-label="Sky over a turquoise sea and sandy beach behind the page"></div>

<header class="site-header">
  <div class="brand">
    <div class="brand-name">Fernbrook Stays</div>
    <div class="brand-tag">at Willowmere Holiday Park</div>
  </div>
  <div class="header-search"><span>Check in date</span><span>Number of Nights</span></div>
  <nav class="main-nav"><span>Home</span><span>News</span><span>Reviews</span><span>Caravans &amp; Lodges</span><span>Payment Plans</span><span>Contact Us</span></nav>
</header>

<div class="hero-photo hero-main" role="img" aria-label="Bright modern lodge lounge with sofas and large windows"></div>
<div class="hero-photo hero-second" role="img" aria-label="Open-plan lodge living room with wooden feature wall"></div>
<div class="hero-copy">
  <h1>PRIVATE HOLIDAY RENTALS</h1>
  <p>Quality Lodge &amp; Caravan hire at Willowmere Holiday Park. Book online today!</p>
</div>

<h2 class="section-title" style="top:720px">LATE DEAL</h2>
<article class="deal-card" style="left:160px">
  <div class="deal-photo" role="img" aria-label="Caravan lounge interior"></div>
  <h3>The Florida Friday 04 September 2015 (3 nights)</h3>
  <div class="deal-meta"><span>Sleeps: 8</span><span>Bedrooms: 3</span></div>
  <span class="btn">Book Now</span>
</article>
<article class="deal-card" style="left:470px">
  <div class="deal-photo" role="img" aria-label="Lodge living area interior"></div>
  <h3>The Allerton Friday 04 September 2015 (3 nights)</h3>
  <div class="deal-meta"><span>Sleeps: 6</span><span>Bedrooms: 3</span></div>
  <span class="btn">Book Now</span>
</article>
<article class="deal-card" style="left:780px">
  <div class="deal-photo" role="img" aria-label="Caravan living room interior"></div>
  <h3>The Allerton Friday 11 September 2015 (3 nights)</h3>
  <div class="deal-meta"><span>Sleeps: 6</span><span>Bedrooms: 3</span></div>
  <span class="btn">Book Now</span>
</article>

<h2 class="section-title" style="top:1280px">OUR CARAVANS AND LODGES</h2>
<article class="lodge-card" style="left:160px">
  <div class="lodge-photo" role="img" aria-label="New Hampshire caravan interior"></div>
  <span class="view-badge">VIEW</span>
  <h3>NEW HAMPSHIRE</h3>
  <div class="lodge-meta"><span>Caravan Type: <b>Lodge</b></span><span>Sleeps: 6</span><span>Grade: <b>Luxury Lodge</b></span><span>Bedrooms: 3</span></div>
</article>
<article class="lodge-card" style="left:470px">
  <div class="lodge-photo" role="img" aria-label="The Winchester caravan interior"></div>
  <span class="view-badge">VIEW</span>
  <h3>THE WINCHESTER</h3>
  <div class="lodge-meta"><span>Caravan Type: <b>Caravan</b></span><span>Sleeps: 8</span><span>Grade: <b>Platinum</b></span><span>Bedrooms: 3</span></div>
</article>
<article class="lodge-card" style="left:780px">
  <div class="lodge-photo" role="img" aria-label="The Allerton caravan interior"></div>
  <span class="view-badge">VIEW</span>
  <h3>THE ALLERTON</h3>
  <div class="lodge-meta"><span>Caravan Type: <b>Caravan</b></span><span>Sleeps: 6</span><span>Grade: <b>Prestige</b></span><span>Bedrooms: 3</span></div>
</article>
<span class="btn view-more">View More</span>
<div class="live-chat">Live Chat</div>

<h2 class="section-title" style="top:1940px">LATEST REVIEW</h2>
<div class="review" style="left:160px;top:2030px"><h4>Consectetur adipiscing elit</h4><div class="stay">Stayed in the Florida</div><p>Lorem ipsum dolor sit amet, consectetur adipiscing elit. Nulla at dolor nec lorem pellentesque vel, pharetra id est.</p></div>
<div class="review" style="left:160px;top:2160px"><h4>Consectetur adipiscing elit</h4><div class="stay">Stayed in the Florida</div><p>Lorem ipsum dolor sit amet, consectetur adipiscing elit. Nulla at dolor nec lorem pellentesque vel, pharetra id est.</p></div>
<div class="review" style="left:160px;top:2290px"><h4>Consectetur adipiscing elit</h4><div class="stay">Stayed in the Florida</div><p>Lorem ipsum dolor sit amet, consectetur adipiscing elit. Nulla at dolor nec lorem pellentesque vel, pharetra id est.</p></div>
<div class="review" style="left:620px;top:2030px"><h4>Consectetur adipiscing elit</h4><div class="stay">Stayed in the Florida</div><p>Lorem ipsum dolor sit amet, consectetur adipiscing elit. Nulla at dolor nec lorem pellentesque vel, pharetra id est.</p></div>
<div class="review" style="left:620px;top:2160px"><h4>Consectetur adipiscing elit</h4><div class="stay">Stayed in the Florida</div><p>Lorem ipsum dolor sit amet, consectetur adipiscing elit. Nulla at dolor nec lorem pellentesque vel, pharetra id est.</p></div>
<div class="review" style="left:620px;top:2290px"><h4>Consectetur adipiscing elit</h4><div class="stay">Stayed in the Florida</div><p>Lorem ipsum dolor sit amet, consectetur adipiscing elit. Nulla at dolor nec lorem pellentesque vel, pharetra id est.</p></div>

<div class="blog-band" role="img" aria-label="Sunny beach with turquoise water and white sand"></div>
<h2 class="section-title" style="top:2556px">RESENT BLOG POST</h2>
<div class="blog-arrows"><span>&#8249;</span><span>&#8250;</span></div>
<p class="blog-intro">Nunc non tincidunt erat. Nam rhoncus, lectus vel tincidunt finibus, tortor nisl porta dolor, vitae rhoncus.</p>
<article class="post" style="left:160px"><div class="post-photo" role="img" aria-label="Lodge veranda overlooking the sea"></div><h5>Aliquet Purus 11/2/2015 11:22</h5><p>Lorem ipsum dolor sit amet, consectetur adipiscing elit. Nulla at dolor nec lorem pellentesque vel.</p></article>
<article class="post" style="left:386px"><div class="post-photo" role="img" aria-label="Caravan kitchen and dining area"></div><h5>Aliquet Purus 11/2/2015 11:22</h5><p>Lorem ipsum dolor sit amet, consectetur adipiscing elit. Nulla at dolor nec lorem pellentesque vel.</p></article>
<article class="post" style="left:612px"><div class="post-photo" role="img" aria-label="Lodge bedroom with sea view"></div><h5>Aliquet Purus 11/2/2015 11:22</h5><p>Lorem ipsum dolor sit amet, consectetur adipiscing elit. Nulla at dolor nec lorem pellentesque vel.</p></article>
<article class="post" style="left:838px"><div class="post-photo" role="img" aria-label="Holiday park lounge with large windows"></div><h5>Aliquet Purus 11/2/2015 11:22</h5><p>Lorem ipsum dolor sit amet, consectetur adipiscing elit. Nulla at dolor nec lorem pellentesque vel.</p></article>

<footer class="site-footer">
  <div class="footer-col" style="left:160px">
    <h6>Important Link</h6>
    <ul><li>Home</li><li>News</li><li>Reviews</li><li>Caravans &amp; Lodges</li><li>2015 Holidays</li></ul>
  </div>
  <div class="footer-col" style="left:340px;top:62px">
    <ul><li>2016 Holidays</li><li>Payment Plans</li><li>Willowmere Park</li><li>Local Attractions</li><li>Contact Us</li></ul>
  </div>
  <div class="footer-col" style="left:520px;width:280px">
    <h6>Contact Info</h6>
    <div class="contact-row"><svg width="12" height="16" viewBox="0 0 12 16"><path d="M6 0a6 6 0 0 0-6 6c0 4.5 6 10 6 10s6-5.5 6-10a6 6 0 0 0-6-6zm0 8.5A2.5 2.5 0 1 1 6 3.5a2.5 2.5 0 0 1 0 5z" fill="#c9cdd0"/></svg><span>Fernbrook Stays, 14 Harbour Lane,<br>Alnmoor, NE66 4QT</span></div>
    <div class="contact-row"><svg width="14" height="14" viewBox="0 0 14 14"><path d="M3 0l3 3-2 2c1 2 3 4 5 5l2-2 3 3-2 3C6 14 0 8 0 2z" fill="#c9cdd0"/></svg><span>01234 567 890</span></div>
    <div class="contact-row"><svg width="14" height="10" viewBox="0 0 14 10"><rect width="14" height="10" fill="#c9cdd0"/><path d="M0 0l7 6 7-6" stroke="#2a2c2e" fill="none"/></svg><span>info@fernbrookstays.com</span></div>
  </div>
  <div class="footer-col" style="left:850px">
    <h6>Social Feed</h6>
    <div class="feed-box"><div class="feed-head"><i></i><span>Fernbrook Stays</span></div></div>
  </div>
</footer>
<div class="copyright">© Copyright 2015 Fernbrook Stays. All rights reserved. Built by Fernbrook Digital</div>
</body>
</html>
```